Tovira Botanics Website Revamping for Ecommerce

Looking to upgrade our website and provide a better experience to users both visually and from a navigation standpoint. Here is our current site

http://toviraleafworks dot com/

Below are some Shopify Design Concepts We Like.
https://lumbergloss. com/pages/classic
https://www.korvabites. com/
https://www.quillmarrowfen. com/

Target Market(s)

People with Darker Skin Tone (Black and Brown)

Industry/Entity Type

Skin Care Product

Number of Pages Required

4 page

Requirements
Must have
• Use the Brand Guide
Nice to have
• Focus on E-Commerce Platforms such as Shopify but can be other platforms too
Should not have
• Don't deviate from Brand Guide (Attached)

```html
<!DOCTYPE html>
<html lang="en">
<head>
<meta charset="utf-8">
<title>Tovira Botanics — Rule Your Skin</title>
<link href="https://fonts.googleapis.com/css2?family=Montserrat:wght@300;400;500;600;700&family=Open+Sans:ital,wght@0,400;0,600;1,400&display=swap" rel="stylesheet">
<style>
:root{
  --green:#1e9a48;
  --green-dark:#0f7a37;
  --brown:#8a3b2b;
  --ink:#333;
  --muted:#888;
  --line:#e6e6e6;
  --white:#fff;
}
*{box-sizing:border-box;margin:0;padding:0}
html,body{width:1200px;height:2684px;overflow:hidden;background:var(--white)}
body{font-family:"Open Sans",sans-serif;color:var(--ink);position:relative}
.page{position:relative;width:1200px;height:2684px;overflow:hidden}

/* hero */
.hero{position:absolute;left:0;top:0;width:1200px;height:600px}
.hero-photo{position:absolute;inset:0;background:
  radial-gradient(ellipse 320px 280px at 760px 200px,#b98a6a 0%,#8a5d44 45%,rgba(80,60,45,0) 75%),
  radial-gradient(ellipse 500px 260px at 900px 500px,#d9b33c 0%,rgba(217,179,60,0) 70%),
  linear-gradient(100deg,#3c3a34 0%,#5b5448 40%,#6d6350 70%,#4e4a3e 100%)}
.hero-edge{position:absolute;left:0;bottom:0;width:1200px;height:140px}
.nav{position:absolute;left:0;top:0;width:1200px;height:110px;display:flex;align-items:center;padding:0 152px}
.brand-name{font-family:"Montserrat",sans-serif;font-weight:600;font-size:34px;color:var(--white);letter-spacing:1px}
.nav-links{margin-left:auto;display:flex;align-items:center;gap:28px;font-family:"Montserrat",sans-serif;font-size:14px;color:var(--white)}
.nav-social{display:flex;gap:10px}
.nav-social span{width:16px;height:16px;border-radius:50%;background:rgba(255,255,255,.85)}
.cart-btn{display:flex;align-items:center;gap:10px;border:1px solid rgba(255,255,255,.6);border-radius:4px;padding:6px 6px 6px 14px}
.cart-btn b{display:block;width:32px;height:24px;border-radius:3px;background:var(--green)}
.hero-copy{position:absolute;left:152px;top:236px;color:var(--white)}
.hero-copy h1{font-family:"Montserrat",sans-serif;font-weight:600;font-size:42px;letter-spacing:1px}
.hero-copy h2{font-family:"Montserrat",sans-serif;font-weight:300;font-size:34px;margin-top:2px}
.hero-list{list-style:none;margin-top:26px;font-size:15px;line-height:28px}
.hero-list li::before{content:"";display:inline-block;width:12px;height:7px;border-left:2px solid var(--white);border-bottom:2px solid var(--white);transform:rotate(-45deg);margin:0 14px 4px 2px}
.btn{display:inline-block;background:var(--green);color:var(--white);font-family:"Montserrat",sans-serif;font-size:14px;font-weight:500;border-radius:20px;padding:10px 28px}
.hero-copy .btn{margin-top:24px}
.hero-arrow{position:absolute;top:186px;width:28px;height:44px;border:2px solid rgba(255,255,255,.8);border-radius:4px}
.hero-arrow.left{left:70px}.hero-arrow.right{right:70px}

/* tiles */
.tiles{position:absolute;left:152px;top:712px;width:896px;height:290px;display:flex;gap:16px}
.tile{flex:1;position:relative;border-radius:2px;overflow:hidden;display:flex;flex-direction:column;align-items:center;justify-content:center;color:var(--white)}
.tile.skin{background:radial-gradient(ellipse at 40% 50%,#b07aa0 0%,#6f8c3e 45%,#2d5a22 100%)}
.tile.ingredients{background:linear-gradient(160deg,#b9d97a 0%,#5e9a3a 50%,#2f6b2a 100%)}
.tile h3{font-family:"Montserrat",sans-serif;font-weight:500;font-size:24px;text-shadow:0 1px 4px rgba(0,0,0,.4)}
.tile .btn{margin-top:70px;padding:8px 24px;font-size:13px}

/* section titles */
.title-rule{width:36px;height:3px;margin:0 auto 14px;background:var(--green);border-radius:2px}
.section-title{font-family:"Montserrat",sans-serif;font-weight:600;font-size:26px;text-align:center;color:var(--ink)}

.featured{position:absolute;left:0;top:1070px;width:1200px}
.products{position:absolute;left:152px;top:1170px;width:896px;display:flex;justify-content:space-between}
.product{width:208px;height:390px;text-align:center;position:relative;padding-top:26px}
.product.active{box-shadow:0 4px 18px rgba(0,0,0,.14);border:1px solid var(--line)}
.bottle{margin:0 auto;background:linear-gradient(90deg,#0a5a26,#1fa04a 45%,#0d6a2e);border-radius:10px 10px 14px 14px}
.product h4{font-family:"Montserrat",sans-serif;font-weight:500;font-size:14px;margin-top:22px}
.stars{color:var(--green);font-size:14px;letter-spacing:2px;margin-top:8px}
.price{font-family:"Montserrat",sans-serif;font-weight:600;font-size:15px;margin-top:8px}
.price s{color:var(--muted);font-weight:400;margin-right:8px}
.ribbon{position:absolute;right:0;top:0;width:0;height:0;border-top:56px solid var(--brown);border-left:56px solid transparent}
.cart-icon{position:absolute;left:50%;bottom:0;transform:translateX(-50%);width:18px;height:16px;border:2px solid var(--green);border-top-width:3px;border-radius:0 0 4px 4px}
.product.active .cart-icon{bottom:-22px;width:44px;height:44px;border:none;border-radius:50%;background:var(--green)}

/* testimonials */
.testimonials{position:absolute;left:0;top:1640px;width:1200px;height:520px}
.testimonials svg.wash{position:absolute;inset:0}
.testimonials .inner{position:absolute;left:0;top:30px;width:1200px;text-align:center}
.avatar{width:76px;height:76px;border-radius:50%;margin:18px auto 0;background:radial-gradient(circle at 50% 40%,#a86e4c,#5a3a2a);border:3px solid var(--white)}
.quote{width:720px;margin:22px auto 0;font-size:16px;line-height:26px;color:var(--ink);position:relative}
.qmark{position:absolute;top:-8px;font-family:"Montserrat",sans-serif;font-weight:700;font-size:72px;color:var(--green);line-height:1}
.qmark.open{left:-96px}.qmark.close{right:-96px}
.author{margin-top:20px;font-family:"Montserrat",sans-serif;font-weight:600;font-size:17px}
.role{font-size:13px;color:#555;font-style:italic}
.dots{display:flex;gap:8px;justify-content:center;margin-top:34px}
.dots span{width:9px;height:9px;border-radius:50%;background:rgba(255,255,255,.7)}
.dots span.on{background:var(--white);outline:2px solid var(--green-dark)}

/* press */
.press{position:absolute;left:152px;top:2272px;width:896px;display:flex;justify-content:space-between;align-items:center;color:#6a6a6a}
.press span{font-family:"Montserrat",sans-serif;font-weight:600;font-size:19px}
.press .boxed{display:block;width:26px;height:26px;background:#9a9a9a}

/* newsletter */
.newsletter{position:absolute;left:0;top:2352px;width:1200px;height:136px;background:linear-gradient(90deg,var(--green-dark),var(--green));display:flex;align-items:center;padding:0 152px;color:var(--white)}
.newsletter h3{font-family:"Montserrat",sans-serif;font-weight:600;font-size:26px}
.newsletter p{font-size:14px;margin-top:4px;opacity:.9}
.signup{margin-left:auto;display:flex;align-items:center;gap:12px}
.signup .field{width:320px;height:36px;border-bottom:1px solid rgba(255,255,255,.7);font-size:13px;padding:8px 4px;opacity:.9}
.signup .send{background:var(--brown);border-radius:18px;padding:9px 22px;font-family:"Montserrat",sans-serif;font-size:13px;font-weight:500}

/* footer */
.footer{position:absolute;left:0;top:2488px;width:1200px;height:196px}
.footer-links{position:absolute;left:152px;top:70px;font-size:13px;color:var(--muted);line-height:28px}
.footer-brand{position:absolute;left:0;width:1200px;top:84px;text-align:center;font-family:"Montserrat",sans-serif;font-weight:600;font-size:46px;color:var(--green)}
.footer-social{position:absolute;right:152px;top:82px;display:flex;gap:12px}
.footer-social span{width:34px;height:34px;border-radius:50%;border:1px solid #bbb}
.footer-social span.on{background:var(--brown);border-color:var(--brown)}
</style>
</head>
<body>
<div class="page">

  <header class="hero">
    <div class="hero-photo" role="img" aria-label="Portrait photograph of a smiling woman with curly hair in a yellow top"></div>
    <nav class="nav">
      <div class="brand-name">Tovira</div>
      <div class="nav-links">
        <span>About Us</span><span>Do Believe</span><span>Contact Us</span>
        <div class="nav-social"><span></span><span></span><span></span><span></span></div>
        <div class="cart-btn">My Cart <b></b></div>
      </div>
    </nav>
    <div class="hero-arrow left"></div>
    <div class="hero-arrow right"></div>
    <div class="hero-copy">
      <h1>RULE YOUR SKIN</h1>
      <h2>In 3 Easy Steps</h2>
      <ul class="hero-list">
        <li>Refresh and clean</li>
        <li>Moisturize and replenish</li>
        <li>Hydrate and soothe</li>
      </ul>
      <span class="btn">Shop Now</span>
    </div>
    <svg class="hero-edge" viewBox="0 0 1200 140" preserveAspectRatio="none">
      <path fill="#fff" d="M0 60 L60 74 L110 58 L170 80 L230 66 L300 88 L360 70 L420 92 L480 78 L540 96 L600 82 L660 100 L720 86 L790 104 L850 88 L910 102 L970 82 L1030 96 L1090 70 L1150 84 L1200 60 L1200 140 L0 140 Z"/>
    </svg>
  </header>

  <section class="tiles">
    <div class="tile skin" role="img" aria-label="Woman in a pink dress standing in a green field">
      <h3>Rule Your Skin</h3><span class="btn">Read More</span>
    </div>
    <div class="tile ingredients" role="img" aria-label="Rows of green tea plantation on rolling hills">
      <h3>Amazing Ingredients</h3><span class="btn">Read More</span>
    </div>
  </section>

  <section class="featured">
    <div class="title-rule"></div>
    <h2 class="section-title">Featured Products</h2>
  </section>

  <section class="products">
    <article class="product">
      <div class="bottle" style="width:64px;height:200px"></div>
      <h4>Purifying Tonic Lotion</h4><div class="stars">★★★★★</div><div class="price">$12.99</div>
      <span class="cart-icon"></span>
    </article>
    <article class="product active">
      <div class="bottle" style="width:62px;height:210px"></div>
      <h4>Facial Cream</h4><div class="stars">★★★★★</div><div class="price">$19.99</div>
      <span class="cart-icon"></span>
    </article>
    <article class="product">
      <div class="bottle" style="width:84px;height:200px"></div>
      <h4>Body Lotion</h4><div class="stars">★★★★★</div><div class="price">$15.99</div>
      <span class="cart-icon"></span>
    </article>
    <article class="product">
      <div class="ribbon"></div>
      <div style="display:flex;gap:12px;justify-content:center;align-items:flex-end;height:200px">
        <div class="bottle" style="width:40px;height:150px;margin:0"></div>
        <div class="bottle" style="width:30px;height:110px;margin:0"></div>
        <div class="bottle" style="width:46px;height:130px;margin:0"></div>
      </div>
      <h4>Tovira Bundle</h4><div class="stars">★★★★★</div><div class="price"><s>$49.97</s>$45.00</div>
      <span class="cart-icon"></span>
    </article>
  </section>

  <section class="testimonials">
    <svg class="wash" viewBox="0 0 1200 520" preserveAspectRatio="none">
      <defs>
        <linearGradient id="washGrad" x1="0" y1="0" x2="0" y2="1">
          <stop offset="0" stop-color="#ffffff"/>
          <stop offset="0.35" stop-color="#cfe9d7"/>
          <stop offset="0.75" stop-color="#3fae63"/>
          <stop offset="1" stop-color="#1e9a48"/>
        </linearGradient>
      </defs>
      <path fill="url(#washGrad)" d="M0 0 H1200 V470 L1140 450 L1080 478 L1010 455 L940 488 L870 460 L800 492 L730 466 L660 496 L590 470 L520 500 L450 472 L380 494 L310 462 L240 488 L170 458 L100 480 L40 456 L0 474 Z"/>
    </svg>
    <div class="inner">
      <div class="title-rule"></div>
      <h2 class="section-title">Testimonials</h2>
      <div class="avatar" role="img" aria-label="Portrait of the customer giving the testimonial"></div>
      <div class="quote">
        <span class="qmark open">“</span>
        I'm constantly on tour but no matter where I go I carry the full Tovira line with me. I simply love the brand plus the feel on my skin is unmatchable
        <span class="qmark close">”</span>
      </div>
      <div class="author">- Maro Delune</div>
      <div class="role">Award winning singer</div>
      <div class="dots"><span></span><span class="on"></span><span></span></div>
    </div>
  </section>

  <section class="press">
    <span>Ledgerly</span>
    <span>Hustlewire</span>
    <span>Coastal Herald</span>
    <i class="boxed"></i>
    <span>Driftline</span>
    <span>Polemark</span>
    <span>Fairbloom</span>
  </section>

  <section class="newsletter">
    <div>
      <h3>Sign Up for Our Newsletter Now</h3>
      <p>To stay in Touch On Our Latest Updates</p>
    </div>
    <div class="signup">
      <div class="field">Enter Your Email</div>
      <span class="send">Send</span>
    </div>
  </section>

  <footer class="footer">
    <div class="footer-links">Shipping · Terms &amp; Conditions · Privacy<br>© 2017 Tovira Botanics. All Rights Reserved</div>
    <div class="footer-brand">Tovira</div>
    <div class="footer-social"><span></span><span class="on"></span><span></span><span></span><span></span></div>
  </footer>

</div>
</body>
</html>
```